Four in One (Flexible infographic for Content Management Industry)

See attachment.
A graphic depicting 4 products, where each can stand on its own and each can be combined with others, but where, if all are taken together, the best result is achieved (the "super product").
Intended use is web. See attached file as an example.
The most basic idea is as the attached diagram shows, where 4 rectangles are arranged in a quadrangle, with a middle rectangle in the center representing the combined 4 products. This concept is fine except it is a bit too obvious as it stands. We are looking for either a variation of this or another concept.
The audience is technical + professional + enterprise - NOT consumers. Hence the design should be conservative in nature.
We are aware of tools like as Canva or Pictogram where such graphics are available, but we are looking for something with a bit more imagination and flexibility.
This graphic should be targeted to web sites and be delivered with vector-based (SVG) graphics.

```html
<!DOCTYPE html>
<html lang="en">
<head>
<meta charset="utf-8">
<title>Super Product</title>
<link rel="stylesheet" href="https://fonts.googleapis.com/css2?family=Bebas+Neue&family=Manrope:wght@400;500&display=swap">
<style>
  :root {
    --bg: #000000;
    --grid: #1c1c1c;
    --card-top: #2e2e2e;
    --card-bottom: #171717;
    --core: #1a1a1a;
    --ink: #ffffff;
    --ink-soft: #d6d6d6;
    --ink-muted: #bdbdbd;
    --accent: #7cff3a;
    --arc-green: #2f6a1c;
    --arc-teal: #173f38;
  }
  * { margin: 0; padding: 0; box-sizing: border-box; }
  html, body { width: 1200px; height: 675px; overflow: hidden; background: var(--bg); }
  .canvas {
    position: relative; width: 1200px; height: 675px; overflow: hidden;
    background-color: var(--bg);
    background-image:
      linear-gradient(var(--grid) 1px, transparent 1px),
      linear-gradient(90deg, var(--grid) 1px, transparent 1px);
    background-size: 72px 72px;
    background-position: 30px 20px;
    font-family: "Manrope", sans-serif;
  }
  .glow {
    position: absolute; left: 250px; top: 60px; width: 720px; height: 580px;
    background: radial-gradient(ellipse at center, #2a2a2a 0%, #111 45%, transparent 75%);
  }
  .decor { position: absolute; left: 0; top: 0; }
  .core {
    position: absolute; left: 388px; top: 160px; width: 436px; height: 336px;
    background: linear-gradient(180deg, #242424, #141414);
    border-radius: 6px;
    box-shadow: 0 0 60px rgba(0,0,0,.8);
  }
  .core-frame {
    position: absolute; left: 370px; top: 148px; width: 468px; height: 362px;
    border: 3px solid #262626; border-radius: 4px;
  }
  .core-title {
    position: absolute; left: 388px; top: 256px; width: 436px;
    text-align: center; font-family: "Bebas Neue", sans-serif;
    font-size: 82px; line-height: 72px; color: var(--ink-soft);
  }
  .card {
    position: absolute; border-radius: 14px;
    background: linear-gradient(160deg, var(--card-top), var(--card-bottom));
    box-shadow: 0 10px 30px rgba(0,0,0,.6);
  }
  .tile { position: absolute; border-radius: 8px; background: linear-gradient(160deg, #303030, #151515); box-shadow: 0 8px 20px rgba(0,0,0,.6); }
  .info { padding: 20px 16px; color: var(--ink-muted); font-size: 8.6px; line-height: 12px; }
  .info p { margin-bottom: 10px; }
  .info ul { list-style: none; }
  .info li { display: flex; align-items: center; gap: 5px; }
  .info li svg { flex: none; }
  .product {
    display: flex; align-items: center; color: var(--ink);
    font-family: "Bebas Neue", sans-serif; font-size: 30px; line-height: 28px;
  }
  .product.stacked { flex-direction: column; justify-content: center; text-align: center; gap: 12px; }
</style>
</head>
<body>
<svg width="0" height="0" style="position:absolute">
  <symbol id="tick" viewBox="0 0 10 10">
    <circle cx="5" cy="5" r="4" fill="none" stroke="#bdbdbd" stroke-width="1"/>
    <path d="M3.2 5.1 L4.5 6.3 L6.9 3.8" fill="none" stroke="#bdbdbd" stroke-width="1"/>
  </symbol>
</svg>
<div class="canvas">
  <div class="glow"></div>

  <svg class="decor" width="1200" height="675" viewBox="0 0 1200 675" aria-hidden="true">
    <path d="M160 462 A55 55 0 0 1 258 440" fill="none" stroke="var(--arc-green)" stroke-width="14"/>
    <path d="M792 72 A60 60 0 0 1 884 66" fill="none" stroke="var(--arc-teal)" stroke-width="12"/>
    <circle cx="350" cy="566" r="50" fill="none" stroke="#1e1e1e" stroke-width="18"/>
  </svg>

  <div class="core-frame"></div>
  <div class="core"></div>
  <div class="core-title">Super<br>Product</div>

  <div class="tile" style="left:242px;top:216px;width:70px;height:70px"></div>
  <div class="tile" style="left:882px;top:224px;width:40px;height:42px"></div>

  <!-- Document management -->
  <div class="card info" style="left:132px;top:73px;width:207px;height:130px">
    <p>Streamline document organization, acces, and collaboration with easier file storage and sharing, leading to more effiecient workflows.</p>
    <ul>
      <li><svg width="8" height="8"><use href="#tick"/></svg>Centralized Document control</li>
      <li><svg width="8" height="8"><use href="#tick"/></svg>Collaborative Workspace Integration</li>
      <li><svg width="8" height="8"><use href="#tick"/></svg>Automated Compliance Tracking</li>
      <li><svg width="8" height="8"><use href="#tick"/></svg>Check 4</li>
    </ul>
  </div>
  <div class="card product" style="left:321px;top:131px;width:209px;height:91px;padding-left:20px;gap:22px">
    <svg width="30" height="42" viewBox="0 0 30 42" aria-hidden="true">
      <path d="M2 2 H20 L28 10 V40 H2 Z" fill="none" stroke="#fff" stroke-width="2"/>
      <path d="M20 2 V10 H28" fill="none" stroke="#fff" stroke-width="2"/>
      <path d="M7 21 H23 M7 26 H23 M7 31 H23" stroke="var(--accent)" stroke-width="2.4"/>
    </svg>
    <div>Document<br>Management</div>
  </div>

  <!-- Security & compliance -->
  <div class="card info" style="left:819px;top:76px;width:261px;height:136px;padding-left:64px">
    <p>Benefit from tailored cloud solutions, secure data storage, and expert disaster recovery planning for reliable and scalable IT operations.</p>
    <ul>
      <li><svg width="8" height="8"><use href="#tick"/></svg>Custom cloud solutions</li>
      <li><svg width="8" height="8"><use href="#tick"/></svg>Secure Data Storage</li>
      <li><svg width="8" height="8"><use href="#tick"/></svg>Expert Disaster Recovery</li>
      <li><svg width="8" height="8"><use href="#tick"/></svg>Check 4</li>
    </ul>
  </div>
  <div class="card product stacked" style="left:737px;top:124px;width:133px;height:138px">
    <svg width="46" height="44" viewBox="0 0 46 44" aria-hidden="true">
      <path d="M10 16 V10 A8 8 0 0 1 26 10 V16" fill="none" stroke="#fff" stroke-width="2"/>
      <path d="M4 16 H32 V40 H4 Z" fill="none" stroke="#fff" stroke-width="2"/>
      <path d="M22 40 H40 A6 6 0 0 0 38 28 A8 8 0 0 0 24 27 A6 6 0 0 0 22 40 Z" fill="#1e1e1e" stroke="var(--accent)" stroke-width="2.4"/>
    </svg>
    <div>Security &amp;<br>Compliance</div>
  </div>

  <!-- ERP -->
  <div class="card info" style="left:104px;top:460px;width:244px;height:130px">
    <p>Simply management across finance, sales and operations, enabling better decision making and improved productivity.</p>
    <ul>
      <li><svg width="8" height="8"><use href="#tick"/></svg>Integrated Business Processes</li>
      <li><svg width="8" height="8"><use href="#tick"/></svg>Enhanced Decision-Making</li>
      <li><svg width="8" height="8"><use href="#tick"/></svg>Productivity Improvement</li>
      <li><svg width="8" height="8"><use href="#tick"/></svg>Check 4</li>
    </ul>
  </div>
  <div class="card product stacked" style="left:318px;top:376px;width:154px;height:186px;gap:16px">
    <svg width="46" height="46" viewBox="0 0 46 46" aria-hidden="true">
      <rect x="2" y="4" width="18" height="18" fill="#bdbdbd"/>
      <rect x="2" y="26" width="18" height="18" fill="#bdbdbd"/>
      <rect x="24" y="26" width="18" height="18" fill="#bdbdbd"/>
      <rect x="27" y="3" width="14" height="14" fill="var(--accent)" transform="rotate(45 34 10)"/>
    </svg>
    <div>Enterprise<br>Resource<br>Planning</div>
  </div>

  <!-- Digital transformation -->
  <div class="card info" style="left:843px;top:446px;width:240px;height:135px;padding-left:47px">
    <p>Turn scanned documents into easily searchable digital archives, boosting efficiency and accessibility.</p>
    <ul>
      <li><svg width="8" height="8"><use href="#tick"/></svg>Instand searchable Archieves with OCR</li>
      <li><svg width="8" height="8"><use href="#tick"/></svg>Automated Docu ment Classification</li>
      <li><svg width="8" height="8"><use href="#tick"/></svg>DocShare and Cloud Blob Ready</li>
      <li><svg width="8" height="8"><use href="#tick"/></svg>Check 4</li>
    </ul>
  </div>
  <div class="card product" style="left:610px;top:455px;width:260px;height:89px;padding-left:12px;gap:14px">
    <svg width="62" height="62" viewBox="0 0 62 62" aria-hidden="true">
      <g stroke="#bdbdbd" stroke-width="2">
        <path d="M31 4 V14 M31 48 V58 M4 31 H14 M48 31 H58 M12 12 L19 19 M43 43 L50 50 M50 12 L43 19 M12 50 L19 43"/>
      </g>
      <g fill="var(--accent)">
        <circle cx="31" cy="4" r="2.5"/><circle cx="31" cy="58" r="2.5"/><circle cx="4" cy="31" r="2.5"/><circle cx="58" cy="31" r="2.5"/>
        <circle cx="12" cy="12" r="2.5"/><circle cx="50" cy="50" r="2.5"/><circle cx="50" cy="12" r="2.5"/><circle cx="12" cy="50" r="2.5"/>
      </g>
      <g fill="none" stroke="var(--accent)" stroke-width="2.4">
        <circle cx="31" cy="31" r="14"/>
        <ellipse cx="31" cy="31" rx="6" ry="14"/>
        <path d="M17 31 H45 M19 24 H43 M19 38 H43"/>
      </g>
    </svg>
    <div>Digital<br>Transformation</div>
  </div>
</div>
</body>
</html>
```